Label for 4oz seasoning

Logo Text

Corvells Seasoning Tastin Real Bold

Logo styles of interest
Wordmark Logo
Colors
3276b5
ec1f27
87cfc6

Requirements
Must have
• Corvells Seasoning
Nice to have
• Tastin Real Bold

```html
<!DOCTYPE html>
<html lang="en">
<head>
<meta charset="utf-8">
<title>Corvells Seasoning – 4oz Label</title>
<link rel="stylesheet" href="https://fonts.googleapis.com/css2?family=Anton&family=Yellowtail&display=swap">
<style>
  :root {
    --label-red: #ec1f27;
    --label-blue: #3276b5;
    --label-teal: #87cfc6;
    --label-white: #ffffff;
    --seed-light: #b98f5c;
    --seed-dark: #6e4a26;
    --page-bg: #ffffff;
  }
  html, body {
    margin: 0;
    width: 1200px;
    height: 1200px;
    overflow: hidden;
    background: var(--page-bg);
  }
  .label {
    position: relative;
    width: 1200px;
    height: 1200px;
  }
  .label-shapes {
    position: absolute;
    inset: 0;
  }
  .brand-name {
    position: absolute;
    left: 100px;
    width: 1000px;
    top: 270px;
    margin: 0;
    text-align: center;
    font-family: "Anton", sans-serif;
    font-weight: 400;
    font-size: 220px;
    line-height: 1;
    letter-spacing: 4px;
    color: var(--label-white);
    text-transform: uppercase;
  }
  .herb-sprig {
    position: absolute;
    left: 530px;
    top: 540px;
    width: 140px;
    height: 22px;
    border-radius: 11px;
    background: rgba(255, 255, 255, 0.55);
  }
  .brand-descriptor {
    position: absolute;
    left: 100px;
    width: 1000px;
    top: 570px;
    margin: 0;
    text-align: center;
    font-family: "Anton", sans-serif;
    font-weight: 400;
    font-size: 100px;
    line-height: 1;
    letter-spacing: 10px;
    color: var(--label-white);
    text-transform: uppercase;
  }
  .tagline {
    position: absolute;
    left: 100px;
    width: 1000px;
    top: 790px;
    margin: 0;
    text-align: center;
    font-family: "Yellowtail", cursive;
    font-size: 96px;
    line-height: 1.05;
    color: var(--label-white);
  }
</style>
</head>
<body>
  <main class="label">
    <svg class="label-shapes" width="1200" height="1200" viewBox="0 0 1200 1200" aria-hidden="true">
      <defs>
        <linearGradient id="seed-fill" x1="0" y1="0" x2="1" y2="0">
          <stop offset="0" stop-color="var(--seed-dark)"/>
          <stop offset="0.3" stop-color="var(--seed-light)"/>
          <stop offset="0.55" stop-color="var(--seed-dark)"/>
          <stop offset="0.8" stop-color="var(--seed-light)"/>
          <stop offset="1" stop-color="var(--seed-dark)"/>
        </linearGradient>
      </defs>
      <!-- product window behind the tagline -->
      <rect x="100" y="730" width="1000" height="330" fill="url(#seed-fill)" role="img" aria-label="Seasoning granules visible through the jar"/>
      <!-- top teal band -->
      <polygon points="100,200 1100,200 1100,245 600,305 100,245" fill="var(--label-teal)"/>
      <!-- red main band -->
      <polygon points="100,235 600,290 1100,235 1100,735 100,735" fill="var(--label-red)"/>
      <!-- blue chevron stripe -->
      <polygon points="100,735 600,700 1100,735 1100,770 600,735 100,770" fill="var(--label-blue)"/>
      <!-- teal chevron stripe -->
      <polygon points="100,770 600,735 1100,770 1100,800 660,770 600,805 540,770 100,800" fill="var(--label-teal)"/>
      <!-- bottom curved bands -->
      <path d="M100,1040 Q600,990 1100,1040 L1100,1060 L100,1060 Z" fill="var(--label-blue)"/>
      <path d="M100,1052 Q600,1008 1100,1052 L1100,1075 L100,1075 Z" fill="var(--label-teal)"/>
    </svg>

    <h1 class="brand-name">Corvells</h1>
    <div class="herb-sprig" role="img" aria-label="Small herb sprig ornament"></div>
    <p class="brand-descriptor">Seasoning</p>
    <p class="tagline">“Tastin’<br>Real Bold”</p>
  </main>
</body>
</html>
```